Webdesign für die Korvelt GmbH
Zielgruppe
Beratung • Renovierung • Reparatur • Planung • Bau • Pflege • Wartung im Bereich der Haustechnik
Aufgabenstellung
Bilder nur von bildmoro oder von der Webseite des Kunden nutzen

```html
<!DOCTYPE html>
<html lang="de">
<head>
<meta charset="utf-8">
<title>Korvelt GmbH – Haustechnik</title>
<link href="https://fonts.googleapis.com/css2?family=Open+Sans:ital,wght@0,400;0,600;0,700;0,800;1,700&display=swap" rel="stylesheet">
<style>
:root{
  --blue:#1c1be6;
  --blue-dark:#15148f;
  --red:#e3232c;
  --ink:#111;
  --text:#555;
  --muted:#777;
  --line:#e6e6e6;
  --grey:#f4f4f4;
  --white:#fff;
}
*{margin:0;padding:0;box-sizing:border-box}
html,body{width:909px;height:1200px;overflow:hidden;background:var(--white)}
body{position:relative;font-family:"Open Sans",sans-serif;color:var(--ink)}
.abs{position:absolute}
a{color:inherit}

.site-header{position:absolute;left:0;top:0;width:909px;height:44px;border-bottom:1px solid var(--line)}
.brand{position:absolute;left:76px;top:9px;font-weight:800;font-size:20px;color:var(--blue);letter-spacing:-.5px;line-height:26px}
.main-nav{position:absolute;top:15px;left:0;width:909px;font-size:8.5px;font-weight:700;letter-spacing:.2px}
.main-nav span{position:absolute;white-space:nowrap}
.search{position:absolute;left:824px;top:16px}

.topbar{position:absolute;left:0;top:44px;width:909px;height:32px;font-size:8.5px;color:var(--muted)}
.topbar .item{position:absolute;top:10px;white-space:nowrap;display:flex;align-items:center;gap:4px}
.send-btn{position:absolute;left:707px;top:0;width:126px;height:32px;background:var(--blue);color:var(--white);font-size:8.5px;font-weight:700;font-style:italic;display:flex;align-items:center;justify-content:center}

.hero{position:absolute;left:0;top:76px;width:909px;height:328px}
.hero-panel{position:absolute;left:0;top:0;width:328px;height:328px;background:var(--blue);overflow:hidden}
.hero-photo{position:absolute;left:328px;top:0;width:581px;height:328px;background:linear-gradient(100deg,#3b5478 0%,#8d9bb0 35%,#e7e4e0 65%,#f2efec 100%)}
.hero-title{position:absolute;left:76px;top:60px;font-size:33px;line-height:38px;font-weight:800;color:var(--white);white-space:nowrap}
.hero-text{position:absolute;left:76px;top:147px;width:225px;font-size:10.5px;line-height:17.7px;color:var(--white);font-weight:600}
.slider-ctrl{position:absolute;left:76px;top:252px;width:89px;height:18px;border-radius:9px;background:var(--blue-dark);color:var(--white);font-size:8.5px;font-weight:700;display:flex;align-items:center;justify-content:center}
.slider-ctrl .arrow{position:absolute;top:0;width:18px;height:18px;border-radius:50%;display:flex;align-items:center;justify-content:center}

.section-title{position:absolute;left:76px;font-size:21px;font-weight:800;display:flex;align-items:center;gap:6px;white-space:nowrap}
.flag{width:11px;height:11px;margin-top:-6px}

.tile{position:absolute;overflow:hidden}
.tile-label{position:absolute;left:24px;font-size:14px;font-weight:700}
.tile-warme{left:76px;top:500px;width:252px;height:106px;background:linear-gradient(90deg,#eef0f3,#f7f7f8)}
.tile-wasser{left:328px;top:500px;width:253px;height:106px;background:var(--blue);color:var(--white)}
.tile-luft{left:581px;top:500px;width:252px;height:106px;background:radial-gradient(circle at 75% 65%,#fafafa 0,#e2e4e7 70%)}
.tile-dach{left:76px;top:606px;width:379px;height:75px;background:linear-gradient(90deg,#dde8f5,#e6edf5)}
.tile-service{left:455px;top:606px;width:378px;height:75px;background:linear-gradient(90deg,#f2ece6,#f5f5f3)}
.tile-wasser .links{position:absolute;left:24px;top:48px;font-size:10px;line-height:26px;width:200px}
.tile-wasser .links a{margin-right:18px}

.intro{position:absolute;left:0;top:745px;width:909px;height:334px;background:var(--grey)}
.intro-text{position:absolute;left:76px;top:96px;width:345px;font-size:10px;line-height:17.7px;color:var(--text)}
.intro-text p{margin-bottom:7px}
.more{position:absolute;left:76px;top:229px;font-size:10px;color:var(--text)}
.service{position:absolute;display:flex;align-items:center;gap:16px;font-size:12.6px;font-weight:600}
.service .ic{width:50px;height:50px;border-radius:50%;background:var(--blue);display:flex;align-items:center;justify-content:center}

.site-footer{position:absolute;left:0;top:1079px;width:909px;height:121px}
.footer-brand{position:absolute;left:76px;top:23px;font-size:13px;font-weight:800;color:var(--blue)}
.footer-nav{position:absolute;right:76px;top:27px;font-size:9px;font-weight:700;color:#666;display:flex;gap:20px}
.footer-meta{position:absolute;top:76px;font-size:8.8px;color:var(--muted);white-space:nowrap;display:flex;align-items:center;gap:4px}
</style>
</head>
<body>

<header class="site-header">
  <div class="brand">KORVELT</div>
  <nav class="main-nav">
    <span style="left:402px">LEISTUNGEN</span>
    <span style="left:496px">FÄLLE</span>
    <span style="left:560px">SERVICETEAM</span>
    <span style="left:658px">KONTAKT</span>
    <span style="left:739px">UBER UNS</span>
  </nav>
  <svg class="search" width="10" height="10" viewBox="0 0 10 10" aria-label="Suche"><circle cx="4.2" cy="4.2" r="3.2" fill="none" stroke="#111" stroke-width="1.3"/><line x1="6.6" y1="6.6" x2="9.2" y2="9.2" stroke="#111" stroke-width="1.3"/></svg>
</header>

<div class="topbar">
  <div class="item" style="left:76px"><svg width="7" height="10" viewBox="0 0 7 10"><rect x=".5" y=".5" width="6" height="9" rx="1" fill="none" stroke="#aaa"/></svg>04512-2870-0</div>
  <div class="item" style="left:163px"><svg width="9" height="9" viewBox="0 0 9 9"><rect x=".5" y="3" width="8" height="5.5" fill="none" stroke="#aaa"/><rect x="2.5" y=".5" width="4" height="3" fill="none" stroke="#aaa"/></svg>04512-2870-29</div>
  <div class="item" style="left:262px"><svg width="7" height="10" viewBox="0 0 7 10"><path d="M3.5 9.5S.5 6 .5 3.5a3 3 0 0 1 6 0C6.5 6 3.5 9.5 3.5 9.5z" fill="none" stroke="#aaa"/></svg>Korvelt Haustechnik GmbH Lindenweg 14 08315 Talheim / Erzg.</div>
  <div class="send-btn">NACHRICHT SENDEN</div>
</div>

<section class="hero">
  <div class="hero-panel">
    <svg class="abs" style="left:76px;top:0" width="252" height="328" viewBox="0 0 252 328"><path d="M0 250 Q20 60 252 0 L0 0 Z" fill="#fff" opacity=".12"/></svg>
  </div>
  <div class="hero-photo" role="img" aria-label="Foto: Installateur bespricht mit einer Kundin in der Küche einen Auftrag"></div>
  <h1 class="hero-title">KORVELT - WE DO THE JOB<br>&amp; DO IT GOOD</h1>
  <p class="hero-text">Wenn Sie einen zuverlässigen Partner für die Erledigung Ihrer Aufträge suchen, Wert auf Kreativität und Freundlichkeit legen, dann sind Sie bei uns an der richtigen Stelle.</p>
  <div class="slider-ctrl">
    <span class="arrow" style="left:0"><svg width="6" height="8" viewBox="0 0 6 8"><path d="M4.5 1L1.5 4l3 3" fill="none" stroke="#fff" stroke-width="1.3"/></svg></span>
    1 of 3
    <span class="arrow" style="right:0;background:#0c0b66"><svg width="6" height="8" viewBox="0 0 6 8"><path d="M1.5 1l3 3-3 3" fill="none" stroke="#fff" stroke-width="1.3"/></svg></span>
  </div>
</section>

<h2 class="section-title" style="top:446px"><svg class="flag" viewBox="0 0 11 11"><path d="M0 0H11L2 3V11H0Z" fill="var(--red)"/></svg>HERZLICH WILLKOMMEN</h2>

<div class="tile tile-warme" role="img" aria-label="Foto: Heizkörper mit Thermostat"><span class="tile-label" style="top:45px">WARME</span></div>
<div class="tile tile-wasser" role="img" aria-label="Wasser">
  <span class="tile-label" style="top:17px">WASSER</span>
  <div class="links"><a>Sanitärtechnik</a><a>Bäder</a><a>Pool</a><br><a>Regenwasser</a></div>
</div>
<div class="tile tile-luft" role="img" aria-label="Foto: Ventilatorgitter"><span class="tile-label" style="top:45px">LUFT</span></div>
<div class="tile tile-dach" role="img" aria-label="Foto: Hausdach"><span class="tile-label" style="top:27px">DACH</span></div>
<div class="tile tile-service" role="img" aria-label="Foto: Rohre und Werkzeug"><span class="tile-label" style="top:27px">SERVICE</span></div>

<section class="intro">
  <h2 class="section-title" style="top:46px"><svg class="flag" viewBox="0 0 11 11"><path d="M0 0H11L2 3V11H0Z" fill="var(--red)"/></svg>HERZLICH WILLKOMMEN</h2>
  <div class="intro-text">
    <p>Wenn Sie einen zuverlässigen Partner für die Erledigung Ihrer Aufträge suchen, Wert auf Kreativität und Freundlichkeit legen, dann sind Sie bei uns an der richtigen Stelle.</p>
    <p>Vom ersten Beratungsgespräch bis zur Übergabe der fertiggestellten Leistung, sollten Sie, wie viele Kunden vor Ihnen, gute Erfahrungen mit uns machen.</p>
  </div>
  <a class="more" style="text-decoration:underline">Mehr sehen</a>

  <div class="service" style="left:480px;top:95px"><span class="ic"><svg width="24" height="24" viewBox="0 0 24 24" fill="none" stroke="#fff" stroke-width="1.3"><rect x="8" y="1" width="8" height="5"/><circle cx="7" cy="11" r="3"/><circle cx="17" cy="11" r="3"/><path d="M1 22c0-4 3-6 6-6s6 2 6 6M11 22c0-4 3-6 6-6s6 2 6 6"/></svg></span>Beratung</div>
  <div class="service" style="left:669px;top:95px"><span class="ic"><svg width="24" height="24" viewBox="0 0 24 24" fill="none" stroke="#fff" stroke-width="1.3"><rect x="2" y="2" width="20" height="20"/><rect x="7" y="8" width="11" height="9"/><line x1="5" y1="2" x2="5" y2="22"/></svg></span>Planung</div>
  <div class="service" style="left:480px;top:159px"><span class="ic"><svg width="24" height="24" viewBox="0 0 24 24" fill="none" stroke="#fff" stroke-width="1.3"><path d="M2 12L12 3l10 9M5 10v11h14V10"/><path d="M9 14a3 3 0 0 1 6 0M15 16a3 3 0 0 1-6 0"/></svg></span>Renovierung</div>
  <div class="service" style="left:669px;top:159px"><span class="ic"><svg width="24" height="24" viewBox="0 0 24 24" fill="none" stroke="#fff" stroke-width="1.3"><rect x="2" y="8" width="8" height="8"/><rect x="14" y="7" width="8" height="10"/><line x1="5" y1="8" x2="5" y2="16"/><line x1="7.5" y1="8" x2="7.5" y2="16"/></svg></span>Construction</div>
  <div class="service" style="left:480px;top:222px"><span class="ic"><svg width="24" height="24" viewBox="0 0 24 24" fill="none" stroke="#fff" stroke-width="1.3"><circle cx="10" cy="10" r="6"/><circle cx="10" cy="10" r="2.5"/><path d="M14 14l8 8"/></svg></span>Reparatur</div>
  <div class="service" style="left:669px;top:222px"><span class="ic"><svg width="24" height="24" viewBox="0 0 24 24" fill="none" stroke="#fff" stroke-width="1.3"><path d="M3 3l18 18M21 3L3 21"/><circle cx="4" cy="20" r="1.5"/></svg></span>Maintenance</div>
</section>

<footer class="site-footer">
  <div class="footer-brand">KORVELT</div>
  <nav class="footer-nav"><span>LEISTUNGEN</span><span>FÄLLE</span><span>SERVICETEAM</span><span>KONTAKT</span><span>UBER UNS</span></nav>
  <div class="footer-meta" style="left:75px">Korvelt Heizung-Sanitär GmbH © 2019</div>
  <div class="footer-meta" style="left:298px"><svg width="7" height="10" viewBox="0 0 7 10"><rect x=".5" y=".5" width="6" height="9" rx="1" fill="none" stroke="#aaa"/></svg>04512-2870-0</div>
  <div class="footer-meta" style="left:386px"><svg width="9" height="9" viewBox="0 0 9 9"><rect x=".5" y="3" width="8" height="5.5" fill="none" stroke="#aaa"/><rect x="2.5" y=".5" width="4" height="3" fill="none" stroke="#aaa"/></svg>04512-2870-29</div>
  <div class="footer-meta" style="right:76px"><svg width="7" height="10" viewBox="0 0 7 10"><path d="M3.5 9.5S.5 6 .5 3.5a3 3 0 0 1 6 0C6.5 6 3.5 9.5 3.5 9.5z" fill="none" stroke="#aaa"/></svg>Korvelt Haustechnik GmbH Lindenweg 14 08315 Talheim / Erzg.</div>
</footer>

</body>
</html>
```